Professional Music Editor Needs a Book Cover Design

I need a book cover design for a series of books which will include excerpts from symphonic pieces required for auditions in professional symphony orchestras. The books will contain text and a lot of music examples. The book will be published in a Brivo and eLeafs version, to be used mainly on an zTab, but will be also available in print in A4 size. The cover may incorporate notation or/and violin images.

The text on the cover should include:

Author: Teodor Markelin D.M.A.
Series: Morning Scales Concert Passages for Violin
Title: Anselm Berlicke, Pale Tower Op. 20, measures 1-62
Updates

Thank you so much for the submitted projects so far! I have uploaded one more photo, which I think may be a good element to use. If you decide to incorporate it, please use just the violin from the photo, not the person. 

And one more thing: I would like the design to be modern, rather than traditional.

Thanks a lot for your work!

Target Market(s)

The target customers of this edition are college students who are going to use the book to prepare for auditions for professional orchestras.

Industry/Entity Type

It Professional

Colors
ffffff

```html
<!DOCTYPE html>
<html lang="en">
<head>
<meta charset="utf-8">
<title>Morning Scales Concert Passages for Violin – Cover</title>
<link rel="stylesheet" href="https://fonts.googleapis.com/css2?family=Questrial&family=Poppins:wght@600;700&display=swap">
<style>
  :root {
    --page-bg: #ffffff;
    --cover-light: #f2f2f3;
    --cover-mid: #d9dadc;
    --cover-edge: #c4c5c8;
    --title-white: #ffffff;
    --band-rust: #a4553b;
    --band-border: #e8c9b8;
    --author-rust: #b2432b;
    --violin-light: #d08a3e;
    --violin-dark: #8a4217;
  }
  * { margin: 0; padding: 0; box-sizing: border-box; }
  html, body {
    width: 1200px;
    height: 900px;
    overflow: hidden;
    background: var(--page-bg);
  }
  .canvas {
    position: relative;
    width: 1200px;
    height: 900px;
  }
  .cover {
    position: absolute;
    left: 313px;
    top: 44px;
    width: 574px;
    height: 811px;
    overflow: hidden;
    background: radial-gradient(ellipse 75% 60% at 45% 58%, var(--cover-light) 0%, var(--cover-mid) 60%, var(--cover-edge) 100%);
  }
  .series-title {
    position: absolute;
    left: 37px;
    top: 40px;
    font-family: "Poppins", sans-serif;
    font-weight: 600;
    font-size: 41px;
    line-height: 38px;
    letter-spacing: 0.5px;
    color: var(--title-white);
    text-transform: uppercase;
  }
  .piece-band {
    position: absolute;
    left: 28px;
    top: 184px;
    width: 520px;
    height: 32px;
    background: var(--band-rust);
    border: 2px solid var(--band-border);
    display: flex;
    align-items: center;
    justify-content: center;
    font-family: "Questrial", sans-serif;
    font-size: 18.5px;
    color: var(--title-white);
    text-transform: uppercase;
    white-space: nowrap;
  }
  .violin-photo {
    position: absolute;
    left: 42px;
    top: 214px;
    width: 234px;
    height: 549px;
    border-radius: 46% 46% 42% 42% / 30% 30% 24% 24%;
    background: radial-gradient(ellipse at 45% 60%, var(--violin-light) 0%, var(--violin-dark) 100%);
  }
  .author {
    position: absolute;
    left: 272px;
    top: 722px;
    font-family: "Poppins", sans-serif;
    font-weight: 700;
    font-size: 17px;
    letter-spacing: -0.3px;
    color: var(--author-rust);
    text-transform: uppercase;
    white-space: nowrap;
  }
</style>
</head>
<body>
  <main class="canvas">
    <section class="cover">
      <h1 class="series-title">Morning Scales<br>Concert Passages<br>for Violin</h1>
      <p class="piece-band">Anselm Berlicke, Pale Tower Op. 20, Measures 1 - 62</p>
      <div class="violin-photo" role="img" aria-label="Photograph of a violin standing upright, front view, with a soft shadow"></div>
      <p class="author">Teodor Markelin D.M.A.</p>
    </section>
  </main>
</body>
</html>
```